Events Calendar and Event Reminder Postcard Design

We need a Calendar of Events and an Event Reminder Postcard that utilize the same design look to create a uniform branding appearance. The design format for the 11" x 17" calendar page should be somewhat similar to the attached calendar sample, but not exactly the same. The 4.25" x 5.5" (4 up on an 8.5"x11" sheet) postcard needs to be able to accommodate the amount of information referenced in the attached example of our existing event reminder postcard. Our logo has been uploaded and should be included on both pieces as well. Prefer Adobe Illustrator files.
Updates

Project Deadline Extended
Reason: Many of the designs need further review

Target Market(s)

TVM Membership

Industry/Entity Type

Events

Font styles to use
Serif
Sans Serif

Requirements
Must have
• See Description and the attached sample files. Prefer Adobe InDesign files
Should not have
• Should not be cartoonish in nature

```html
<!DOCTYPE html>
<html lang="en">
<head>
<meta charset="utf-8">
<title>TVM 2017 Calendar of Events</title>
<link href="https://fonts.googleapis.com/css2?family=Montserrat:wght@400;600;700&family=Questrial&family=Josefin+Sans:wght@400;600&display=swap" rel="stylesheet">
<style>
  :root {
    --taupe: #5e5953;
    --sage: #7f9a94;
    --ink: #3d3a36;
    --page: #ffffff;
    --backdrop: #f3f3f3;
    --rule: #b9b6b2;
  }
  * { box-sizing: border-box; margin: 0; padding: 0; }
  html, body { width: 1200px; height: 1000px; overflow: hidden; background: var(--backdrop); }
  .canvas { position: relative; width: 1200px; height: 1000px; }
  .sheet { position: absolute; left: 325px; top: 15px; width: 633px; height: 980px; background: var(--page); overflow: hidden; }

  .title-band { position: absolute; left: 0; top: 7px; width: 390px; height: 66px; }
  .title-year { position: absolute; left: 24px; top: 10px; font-family: "Questrial", sans-serif; font-size: 52px; line-height: 52px; color: var(--sage); letter-spacing: -1px; }
  .title-text { position: absolute; left: 152px; top: 11px; font-family: "Questrial", sans-serif; font-size: 26px; line-height: 29px; color: #fff; letter-spacing: 0.5px; }

  .org { position: absolute; left: 23px; top: 85px; font-family: "Montserrat", sans-serif; color: var(--ink); }
  .org-name { font-weight: 600; font-size: 13.5px; line-height: 18px; color: var(--taupe); }
  .org-line { font-size: 12px; line-height: 15px; margin-top: 3px; }
  .org-line + .org-line { margin-top: 0; }
  .org-label { color: var(--sage); font-weight: 600; }
  .org-web { color: var(--sage); font-weight: 700; font-size: 12px; line-height: 15px; letter-spacing: 0.3px; }

  .brand { position: absolute; left: 438px; top: 60px; display: flex; align-items: center; gap: 10px; }
  .brand-mark { width: 22px; height: 22px; background: var(--sage); }
  .brand-name { font-family: "Montserrat", sans-serif; font-weight: 700; font-size: 48px; line-height: 48px; color: var(--taupe); letter-spacing: 2px; }

  .divider { position: absolute; left: 0; top: 170px; width: 633px; height: 1px; background: var(--rule); }

  .column { position: absolute; top: 0; width: 200px; height: 980px; }
  .column-1 { left: 8px; }
  .column-2 { left: 226px; }
  .column-3 { left: 437px; }

  .month { position: absolute; left: 0; font-family: "Josefin Sans", sans-serif; font-weight: 400; font-size: 18px; line-height: 18px; color: var(--taupe); letter-spacing: 0.2px; }
  .event { position: absolute; left: 0; display: flex; }
  .day { width: 55px; font-family: "Questrial", sans-serif; font-size: 33px; line-height: 33px; color: var(--sage); letter-spacing: -0.5px; }
  .note { width: 140px; border-left: 1px solid var(--taupe); padding: 3px 0 1px 4px; font-family: "Montserrat", sans-serif; font-size: 7px; line-height: 9.3px; color: var(--ink); }
  .note b { font-weight: 700; }

  .foot-band { position: absolute; left: 0; bottom: 10px; width: 633px; height: 7px; background: var(--taupe); }
</style>
</head>
<body>
<div class="canvas">
  <main class="sheet">
    <header>
      <svg class="title-band" viewBox="0 0 390 66" aria-hidden="true"><polygon points="0,0 300,0 390,66 0,66" fill="var(--taupe)"/></svg>
      <div class="title-year">2017</div>
      <h1 class="title-text">CALENDAR<br>OF EVENTS</h1>
      <div class="org">
        <p class="org-name">Timber Valley Makers Guild of Linden &amp; Ash Counties</p>
        <p class="org-line">1480 Cedarline Ave SE Suite #210, Brookfield OR 97000</p>
        <p class="org-line"><span class="org-label">Phone:</span> (555) 014-2200 &nbsp;<span class="org-label">Fax:</span> (555) 014-2271</p>
        <p class="org-web">www.timbervalleymakers.org</p>
      </div>
      <div class="brand"><span class="brand-mark"></span><span class="brand-name">TVM</span></div>
    </header>
    <div class="divider"></div>

    <section class="column column-1">
      <h2 class="month" style="top:187px">JANUARY</h2>
      <div class="event" style="top:213px"><span class="day">02</span><p class="note"><b>Lorem ipsum</b> dolor sit amet, consectetur adipiscing elit, sed do eiusmod tempor incididunt ut labore et tetur adipiscing elit, sed do eiusmod dolor sit amet, consectetur adipiscing elit, sed do eiusmod tempor incididunt ut labore et tetur adipiscing elit, sed do eiusmod</p></div>
      <div class="event" style="top:293px"><span class="day">12</span><p class="note"><b>Lorem ipsum</b> dolor sit amet, consectetur adipiscing elit, sed do eiusmod tempor incididunt ut labore et tetur adipiscing elit, sed dolor sit amet, consectetur adipiscing elit, sed do eiusmod tempor incididunt ut labore et tetur adipiscing elit, sed do eiusmod</p></div>
      <div class="event" style="top:373px"><span class="day">30</span><p class="note"><b>Lorem ipsum</b> dolor sit amet, consectetur adipiscing elit, sed do eiusmod tempor incididunt ut labore et tetur adipiscing elit, sed do eiusmod</p></div>
      <h2 class="month" style="top:423px">FEBRUARY</h2>
      <div class="event" style="top:449px"><span class="day">27</span><p class="note"><b>Lorem ipsum</b> dolor sit amet, consectetur adipiscing elit, sed do eiusmod</p></div>
      <div class="event" style="top:493px"><span class="day">25</span><p class="note"><b>Lorem ipsum</b> dolor sit amet, consectetur adipiscing elit, sed do eiusmod tempor incididunt ut labore et tetur adipiscing elit, sed do eiusmod consectetur adipiscing elit, sed do eiusmod tempor incididunt ut labore et tetur adipiscing elit, sed do eiusmod</p></div>
      <h2 class="month" style="top:579px">MARCH</h2>
      <div class="event" style="top:605px"><span class="day">08</span><p class="note"><b>Lorem ipsum</b> dolor sit amet, consectetur adipiscing elit, sed do eiusmod tempor incididunt ut labore et</p></div>
      <div class="event" style="top:657px"><span class="day">19</span><p class="note"><b>Lorem ipsum</b> dolor sit amet, consectetur adipiscing elit, sed do eiusmod tempor incididunt ut labore et tetur adipiscing elit, sed do eiusmod</p></div>
      <div class="event" style="top:713px"><span class="day">23</span><p class="note"><b>Lorem ipsum</b> dolor sit amet, consectetur adipiscing elit, sed do eiusmod tempor incididunt ut labore et tetur adipiscing elit, sed do eiusm consectetur adipiscing elit, sed do eiusmod tempor incididunt ut labore et tetur adipiscing elit, sed do eiusmod</p></div>
      <h2 class="month" style="top:782px">APRIL</h2>
      <div class="event" style="top:807px"><span class="day">03</span><p class="note"><b>Lorem ipsum</b> dolor sit amet, consectetur adipiscing elit, sed do eiusmod tempor incididunt ut labore et</p></div>
      <div class="event" style="top:858px"><span class="day">13</span><p class="note"><b>Lorem ipsum</b> dolor sit amet, consectetur adipiscing elit, sed do eiusmod tempor incididunt ut labore et tetur adipiscing elit, sed do eiusmod</p></div>
    </section>

    <section class="column column-2">
      <h2 class="month" style="top:187px">MAY</h2>
      <div class="event" style="top:211px"><span class="day">01</span><p class="note"><b>Lorem ipsum</b> dolor sit amet, consectetur adipiscing elit, sed do eiusmod tempor incididunt ut labore et</p></div>
      <div class="event" style="top:263px"><span class="day">23</span><p class="note"><b>Lorem ipsum</b> dolor sit amet, consectetur adipiscing elit, sed do eiusmod tempor incididunt ut labore et tetur adipiscing elit, sed do eiusmod</p></div>
      <h2 class="month" style="top:328px">JUNE</h2>
      <div class="event" style="top:353px"><span class="day">10</span><p class="note"><b>Lorem ipsum</b> dolor sit amet, consectetur adipiscing elit, sed do eiusmod tempor incididunt ut labore et</p></div>
      <div class="event" style="top:405px"><span class="day">25</span><p class="note"><b>Lorem ipsum</b> dolor sit amet, consectetur adipiscing elit, sed do eiusmod tempor incididunt ut labore et tetur adipiscing elit, sed do eiusmod</p></div>
      <h2 class="month" style="top:467px">JULY</h2>
      <div class="event" style="top:493px"><span class="day">05</span><p class="note"><b>Lorem ipsum</b> dolor sit amet, consectetur adipiscing elit, sed do eiusmod tempor incididunt ut labore et</p></div>
      <div class="event" style="top:544px"><span class="day">17</span><p class="note"><b>Lorem ipsum</b> dolor sit amet, consectetur adipiscing elit, sed do eiusmod tempor incididunt ut labore et tetur adipiscing elit, sed do eiusmod</p></div>
      <div class="event" style="top:600px"><span class="day">22</span><p class="note"><b>Lorem ipsum</b> dolor sit amet, consectetur adipiscing elit, sed do eiusmod tempor incididunt ut labore et tetur adipiscing elit, sed do eiusmod</p></div>
      <h2 class="month" style="top:662px">AUGUST</h2>
      <div class="event" style="top:688px"><span class="day">09</span><p class="note"><b>Lorem ipsum</b> dolor sit amet, consectetur adipiscing elit, sed do eiusmod tempor incididunt ut labore et</p></div>
      <div class="event" style="top:739px"><span class="day">23</span><p class="note"><b>Lorem ipsum</b> dolor sit amet, consectetur adipiscing elit, sed do eiusmod tempor incididunt ut labore et tetur adipiscing elit, sed do eiusmod</p></div>
      <div class="event" style="top:804px"><span class="day">31</span><p class="note"><b>Lorem ipsum</b> dolor sit amet, consectetur adipiscing elit, sed do eiusmod tempor incididunt ut labore et tetur adipiscing elit, sed do eiusmod</p></div>
    </section>

    <section class="column column-3">
      <h2 class="month" style="top:188px">SEPTEMBER</h2>
      <div class="event" style="top:213px"><span class="day">01</span><p class="note"><b>Lorem ipsum</b> dolor sit amet, consectetur adipiscing elit, sed do eiusmod tempor incididunt ut labore et</p></div>
      <div class="event" style="top:265px"><span class="day">12</span><p class="note"><b>Lorem ipsum</b> dolor sit amet, consectetur adipiscing elit, sed do eiusmod tempor incididunt ut labore et tetur adipiscing elit, sed do eiusmod</p></div>
      <div class="event" style="top:321px"><span class="day">20</span><p class="note"><b>Lorem ipsum</b> dolor sit amet, consectetur adipiscing elit, sed do eiusmod tempor incididunt ut labore et tetur adipiscing elit, sed do eiusmod</p></div>
      <h2 class="month" style="top:389px">OCTOBER</h2>
      <div class="event" style="top:415px"><span class="day">17</span><p class="note"><b>Lorem ipsum</b> dolor sit amet, consectetur adipiscing elit, sed do eiusmod tempor incididunt ut labore et</p></div>
      <div class="event" style="top:466px"><span class="day">26</span><p class="note"><b>Lorem ipsum</b> dolor sit amet, consectetur adipiscing elit, sed do eiusmod tempor incididunt ut labore et tetur adipiscing elit, sed do eiusmod</p></div>
      <h2 class="month" style="top:525px">NOVEMBER</h2>
      <div class="event" style="top:552px"><span class="day">12</span><p class="note"><b>Lorem ipsum</b> dolor sit amet, consectetur adipiscing elit, sed do eiusmod tempor incididunt ut labore et</p></div>
      <div class="event" style="top:602px"><span class="day">19</span><p class="note"><b>Lorem ipsum</b> dolor sit amet, consectetur adipiscing elit, sed do eiusmod tempor incididunt ut labore et tetur adipiscing elit, sed do eiusmod</p></div>
      <div class="event" style="top:658px"><span class="day">24</span><p class="note"><b>Lorem ipsum</b> dolor sit amet, consectetur adipiscing elit, sed do eiusmod tempor incididunt ut labore et tetur adipiscing elit, sed do eiusmod</p></div>
      <h2 class="month" style="top:727px">DECEMBER</h2>
      <div class="event" style="top:752px"><span class="day">07</span><p class="note"><b>Lorem ipsum</b> dolor sit amet, consectetur adipiscing elit, sed do eiusmod tempor incididunt ut labore et</p></div>
      <div class="event" style="top:803px"><span class="day">29</span><p class="note"><b>Lorem ipsum</b> dolor sit amet, consectetur adipiscing elit, sed do eiusmod tempor incididunt ut labore et tetur adipiscing elit, sed do eiusmod</p></div>
    </section>

    <div class="foot-band"></div>
  </main>
</div>
</body>
</html>
```